Save The Date for 2019 RLX Colloquium

We have an annual meeting each June and need a Save the Date (STD) designed. It should be a two-sided postcard with room for address and stamp (according to US Mail postal standards). I have attached some examples from prior years, but we would appreciate a more modern and attractive design for this year's STD.

Target Market(s)

Our own members - nurses, nurse practitioners, PAs and physicians

Industry/Entity Type

Medical

Requirements
Must have
• Must include our logos (attached), ideally in a coordinating fashion - as was done in prior years (see examples attached) and without modifying the logos too much. Needs have the following information:
• - "Save the Date"
• - "The 12th Annual Heartline Crew Colloquium"
• - "Friday, June 7, 2019" or "6/7/19"
• - "The Varrick–Dunmore Building | 318 West 57th Street | NYC"
• - Please include our website (www.qb-zrh.org/events), phone number (212-555-0147) and email address (ask@qb-zrh.org) for people to ask questions
• - Must have space for a postage stamp and the name/address of the postcard recipient
Nice to have
• Would be nice to remain in our blue/grey/olive color palate (see attached Brand Standards guide).
Should not have
• Please do not use stock photos of medical staff. Please don't use cartoons or cartoon images (although a tasteful sketch may be considered).

```html
<!DOCTYPE html>
<html lang="en">
<head>
<meta charset="utf-8">
<title>Save the Date – 2019 RLX Colloquium</title>
<link rel="stylesheet" href="https://fonts.googleapis.com/css2?family=Libre+Franklin:wght@400;500;700;800;900&family=Roboto+Condensed:wght@400&display=swap">
<style>
  :root {
    --stage-dark: #2e2e2e;
    --stage-light: #575757;
    --brand-blue: #1f8dcc;
    --brand-navy: #1b2f5c;
    --paper: #ffffff;
    --sketch-pale: #dde4ee;
    --sketch-blue: #d7e6f4;
  }
  * { box-sizing: border-box; margin: 0; padding: 0; }
  html, body { width: 1200px; height: 529px; overflow: hidden; }
  body {
    position: relative;
    background: linear-gradient(to bottom, var(--stage-dark) 0 376px, var(--stage-light) 376px 100%);
    font-family: "Libre Franklin", Arial, sans-serif;
  }
  .postcard {
    position: absolute; top: 54px; width: 538px; height: 421px;
    background: var(--paper); overflow: hidden;
  }
  .postcard--front { left: 55px; }
  .postcard--back { left: 607px; }

  /* Front */
  .front-watermark-art {
    position: absolute; left: 250px; top: 0; width: 288px; height: 421px;
    background: radial-gradient(ellipse at 60% 50%, var(--sketch-pale) 0%, rgba(221,228,238,0.55) 50%, rgba(221,228,238,0) 78%);
  }
  .front-art {
    position: absolute; left: 0; top: 0; width: 208px; height: 278px;
    background: var(--brand-blue);
  }
  .front-art__sketch {
    position: absolute; left: 28px; top: 12px; width: 160px; height: 252px;
    border-radius: 42% 46% 48% 40%;
    background: radial-gradient(ellipse at 50% 55%, var(--sketch-blue) 0%, rgba(215,230,244,0.4) 65%, rgba(215,230,244,0) 100%);
  }
  .partners {
    position: absolute; left: 0; top: 278px; width: 208px; height: 143px;
    background: var(--brand-navy);
  }
  .partner {
    position: absolute; left: 31px; display: flex; align-items: center; gap: 8px;
  }
  .partner:nth-child(1) { top: 15px; }
  .partner:nth-child(2) { top: 55px; }
  .partner:nth-child(3) { top: 95px; }
  .partner__mark {
    width: 34px; height: 34px; border-radius: 50%;
    border: 1.5px solid rgba(255,255,255,0.85); flex: none;
  }
  .partner__text { color: #fff; font-size: 6.6px; line-height: 8.4px; }
  .partner__role { display: block; opacity: 0.8; }

  .front-copy { position: absolute; left: 231px; top: 0; width: 300px; color: var(--brand-navy); }
  .front-copy > * { position: absolute; left: 0; white-space: nowrap; }
  .headline { top: 24px; font-weight: 900; font-size: 50px; line-height: 51px; letter-spacing: 0.3px; }
  .edition { top: 190px; color: var(--brand-blue); font-weight: 800; font-size: 28px; line-height: 30px; }
  .event-title {
    top: 221px; width: 218px; color: var(--brand-blue); font-weight: 700; font-size: 10.6px;
    line-height: 13px; padding-bottom: 3px; border-bottom: 1.5px solid var(--brand-navy);
  }
  .event-extra { top: 245px; color: var(--brand-blue); font-weight: 700; font-size: 10.4px; line-height: 14px; }
  .event-date {
    top: 292px; width: 180px; font-weight: 700; font-size: 13.4px; line-height: 16px;
    padding-bottom: 3px; border-bottom: 1.5px solid var(--brand-navy);
  }
  .event-venue {
    top: 313px; width: 180px; font-size: 12.2px; line-height: 16px; font-weight: 500;
    padding-bottom: 3px; border-bottom: 1.5px solid var(--brand-navy);
  }
  .event-contact { top: 351px; font-size: 12.4px; line-height: 16px; font-weight: 500; }

  /* Back */
  .sender {
    position: absolute; left: 0; top: 0; width: 233px; height: 107px;
    background: var(--brand-navy); color: #fff;
    display: flex; align-items: center; padding-left: 19px; gap: 10px;
  }
  .sender__mark { width: 56px; height: 56px; border-radius: 50%; border: 2px solid #fff; flex: none; }
  .sender__divider { width: 1px; height: 54px; background: rgba(255,255,255,0.7); flex: none; }
  .sender__name { font-size: 14px; line-height: 16px; }
  .sender__unit { font-size: 6.6px; letter-spacing: 0.8px; margin-bottom: 1px; text-transform: uppercase; }
  .sender__address { font-family: "Roboto Condensed", Arial, sans-serif; font-size: 8.4px; line-height: 10.5px; }

  .invitation {
    position: absolute; left: 0; top: 107px; width: 233px; height: 314px;
    background: var(--brand-blue); color: #fff;
    padding: 19px 22px 0 18px;
    font-family: "Roboto Condensed", Arial, sans-serif; font-size: 8.5px; line-height: 13px;
  }
  .invitation p { margin-bottom: 13px; }

  .stamp-box {
    position: absolute; left: 441px; top: 42px; width: 70px; height: 70px;
    border: 1.5px solid var(--brand-navy);
  }
  .address-line {
    position: absolute; left: 283px; width: 228px; height: 0;
    border-top: 1.5px solid var(--brand-navy);
  }
  .address-line--1 { top: 312px; }
  .address-line--2 { top: 345px; }
  .address-line--3 { top: 379px; }
</style>
</head>
<body>

<section class="postcard postcard--front" aria-label="Postcard front">
  <div class="front-watermark-art" role="img" aria-label="Faint engraved anatomical heart sketch"></div>
  <div class="front-art">
    <div class="front-art__sketch" role="img" aria-label="Engraved anatomical heart sketch in pale blue"></div>
  </div>

  <div class="partners">
    <div class="partner">
      <span class="partner__mark"></span>
      <p class="partner__text"><span class="partner__role">Presented by</span>The Hudson<br>Cardiological Society, Inc.</p>
    </div>
    <div class="partner">
      <span class="partner__mark"></span>
      <p class="partner__text"><span class="partner__role">of the</span>Hudson State Chapter,<br>Ridgeline College of Heart Medicine</p>
    </div>
    <div class="partner">
      <span class="partner__mark"></span>
      <p class="partner__text"><span class="partner__role">In association with</span>Harborview Cardiac Center</p>
    </div>
  </div>

  <div class="front-copy">
    <h1 class="headline">SAVE<br>THE<br>DATE</h1>
    <p class="edition">12TH ANNUAL</p>
    <p class="event-title">HEARTLINE CREW COLLOQUIUM</p>
    <p class="event-extra">and First-Ever QBZRH Summer Soirée,<br>featuring Rex and the Rhythm Crew</p>
    <p class="event-date">Friday, June 7, 2019</p>
    <p class="event-venue">The Varrick–Dunmore Building<br>318 West 57th Street &nbsp;|&nbsp; NYC</p>
    <p class="event-contact">www.qb-zrh.org/events<br>212-555-0147<br>Email: ask@qb-zrh.org</p>
  </div>
</section>

<section class="postcard postcard--back" aria-label="Postcard back">
  <div class="sender">
    <span class="sender__mark"></span>
    <span class="sender__divider"></span>
    <div>
      <p class="sender__name">Hudson State</p>
      <p class="sender__unit">Chapter</p>
      <p class="sender__address">730 Larkin Avenue, Ste. 410<br>New York, NY 10022</p>
    </div>
  </div>

  <article class="invitation">
    <p>Join us for great events at The Varrick–Dunmore Building, 318 West 57th Street | NYC, New York, this June!</p>
    <p>Now in its tenth year, the Annual Heartline Crew (RLX) Colloquium is a unique all-day academic event designed to enhance current knowledge about the etiology, prevention, intervention and management of cardiovascular disease.</p>
    <p>In the evening, the Hudson State Chapter of the RCHM will host its first-ever Summer Soirée, featuring the band Rex &amp; the Rhythm Crew playing us off into the night.</p>
    <p>A courtesy block of rooms has already been secured at The Inn for these two events. To reserve a room at the discounted rate, please call (800) 555-0192 and be sure to mention “The Hudson Cardiological Society.”</p>
  </article>

  <div class="stamp-box" aria-label="Stamp area"></div>
  <span class="address-line address-line--1"></span>
  <span class="address-line address-line--2"></span>
  <span class="address-line address-line--3"></span>
</section>

</body>
</html>
```